Web Design Project for Energy Efficiency Consultancy

We require a website designed and preferably coded. The website will have around 6-8 pages of basic content with a "contact us" webform.

We are primarily after someone to take our logo, colour scheme and the rough layouts that we have produced and to turn them into a professional looking website.

Please refer to the attached documents for example layouts that we have put together in photoshop, example content, our logo and colour scheme.

We will accept a PSD file but our preference is certainly to have it coded.
Updates

We have attached some documents to the brief that provide more detail.

We have had a question about how projects can be loaded into Harbor Widget. Follow this link for more info http://www.harborwidget-example.com.au/support/dw#install

Target Market(s)

Builders, real estate agents, government agencies

Industry/Entity Type

It Professional

Requirements
Must have
• We are after a clean and professional look.
Nice to have
• We are keen to have the site fully coded in harbor widget as we have another website that has been built on HW and so we are familiar with how to use it.

```html
<!DOCTYPE html>
<html lang="en">
<head>
<meta charset="utf-8">
<title>Verdant Watt</title>
<link href="https://fonts.googleapis.com/css2?family=Arimo:wght@400&family=Tinos:wght@400&display=swap" rel="stylesheet">
<style>
:root{
  --orange:#f5640f;
  --green:#7ab800;
  --gold:#e3a700;
  --cream-top:#fffbe8;
  --header-warm:#fed98a;
  --content-bg:#fec24c;
  --panel:#fbf39a;
  --dark:#2b1a05;
  --button:#3d2103;
  --text:#4a300c;
  --link:#7a4a12;
  --rule:#b07a1e;
  --white:#ffffff;
  --photo:#b9c3c6;
  --thumb:#c4cbd0;
}
*{box-sizing:border-box;margin:0;padding:0}
html,body{width:1180px;height:1200px;overflow:hidden;background:var(--dark)}
body{font-family:"Arimo",Arial,sans-serif;color:var(--text)}
h2,h3{font-weight:400}
.page{position:relative;width:1180px;height:1200px;overflow:hidden;background:var(--dark)}
.abs{position:absolute}

.header{left:0;top:0;width:1180px;height:121px;background:linear-gradient(90deg,var(--cream-top) 0%,#fff3cf 40%,var(--header-warm) 100%)}
.brand-name{left:186px;top:40px;font-family:"Tinos",serif;font-size:36px;line-height:36px;color:#d9a100}

.main-nav{left:440px;top:15px;width:555px;height:91px;border-radius:10px;background:linear-gradient(180deg,#ffa12a,#ff6a0a)}
.nav-item{position:absolute;display:flex;align-items:center;gap:12px;color:#fff7e0;font-family:"Tinos",serif;font-size:15px;height:32px}
.nav-item svg{flex:none}
.nav-item.active{left:18px;top:10px;width:125px;border-radius:8px;background:linear-gradient(180deg,#b6e24a,#64b300);padding-left:7px;gap:26px}

.hero{left:0;top:121px;width:1180px;height:459px;background:var(--photo)}

.feature{top:427px;width:253px;height:127px;color:var(--white)}
.feature.residential{left:185px;background:var(--orange)}
.feature.commercial{left:464px;background:var(--green)}
.feature.experience{left:742px;background:var(--gold)}
.feature-thumb{position:absolute;left:7px;top:9px;width:110px;height:110px;border:3px solid var(--white);background:var(--thumb)}
.feature-title{position:absolute;left:128px;top:28px;font-family:"Tinos",serif;font-size:17px;line-height:20px}
.btn{position:absolute;background:var(--button);color:#fff;font-size:10.5px;display:flex;align-items:center;justify-content:center}
.feature .btn{left:150px;top:78px;width:67px;height:25px}

.content{left:0;top:580px;width:1180px;height:491px;background:var(--content-bg)}
.section-title{font-family:"Tinos",serif;font-size:17px;color:#2e1d05;line-height:20px}
.welcome-title{left:184px;top:608px}
.welcome-body{left:185px;top:644px;width:255px;font-size:10px;line-height:14.8px;text-align:justify;color:#3d2a0c}
.welcome-thumb{float:left;width:120px;height:83px;border:3px solid #fff;margin:2px 8px 2px 0;background:var(--thumb)}
.welcome-more{left:368px;top:847px;width:67px;height:25px}
.divider{left:457px;top:632px;width:1px;height:203px;background:#e6a93a}
.services-title{left:482px;top:608px}
.service-list{list-style:none;position:absolute;top:635px}
.service-list li{height:25.3px;display:flex;align-items:center;gap:11px;font-size:10.5px;color:#3d2a0c;border-bottom:1px dotted var(--rule)}
.service-list li:last-child{border-bottom:none}
.service-list.first{left:480px;width:241px}
.service-list.second{left:750px;width:243px}
.services-more{left:927px;top:847px;width:68px;height:25px}

.footer-band{left:0;top:1071px;width:1180px;height:129px;background:var(--dark)}
.info-panel{left:185px;top:890px;width:812px;height:238px;border-radius:10px;background:var(--panel);box-shadow:0 2px 0 #c9bb6a}
.col-rule{position:absolute;top:20px;width:1px;height:205px;background:#efe08a}
.panel-title{position:absolute;top:25px;font-family:"Tinos",serif;font-size:16px;color:#3a2608}
.link-list{list-style:none;position:absolute;left:18px;top:62px}
.link-list li{height:25.3px;display:flex;align-items:center;gap:12px;font-size:10.5px;color:var(--link)}
.news-item{position:absolute;left:180px;display:flex;gap:8px}
.news-date{width:49px;height:49px;background:var(--dark);color:#fff;font-family:"Tinos",serif;text-align:center;line-height:15px;padding-top:10px;font-size:12px}
.news-date b{display:block;font-weight:400;font-size:20px;line-height:18px}
.news-text{width:125px;font-size:10.5px;line-height:13.5px;color:var(--link);padding-top:3px}
.pager{position:absolute;top:187px;width:26px;height:26px;border-radius:50%;display:flex;align-items:center;justify-content:center}
.enquiry{position:absolute;left:401px;top:64px;font-size:10.5px;line-height:18.5px;color:var(--link)}
.enquiry .row{display:flex}
.enquiry .k{width:90px}
.enquiry .s{width:20px}
.form-label{position:absolute;left:620px;font-size:10.5px;color:#5a3a10}
.field{position:absolute;left:678px;width:116px;height:21px;border-radius:3px;background:var(--button)}
.submit{left:726px;top:194px;width:68px;height:25px}

.copyright{left:190px;top:1156px;font-size:10.5px;color:#6b4a1e}
.social{top:1151px;width:26px;height:26px;border-radius:50%;background:#8a5a14}
</style>
</head>
<body>
<div class="page">

  <header class="header abs"></header>
  <div class="brand-name abs">Verdant Watt</div>

  <nav class="main-nav abs">
    <div class="nav-item active">
      <svg width="17" height="17" viewBox="0 0 17 17"><circle cx="8.5" cy="8.5" r="8.5" fill="#fff"/><path d="M6 5.5l3 3-3 3M9 5.5l3 3-3 3" stroke="#7ab800" stroke-width="1.2" fill="none"/></svg>
      <span>HOME</span>
    </div>
    <div class="nav-item" style="left:170px;top:10px">
      <svg width="17" height="17" viewBox="0 0 17 17"><circle cx="8.5" cy="8.5" r="8.5" fill="#fff"/><path d="M6 5.5l3 3-3 3M9 5.5l3 3-3 3" stroke="#f5640f" stroke-width="1.2" fill="none"/></svg>
      <span>COMMERCIAL SERVICE</span>
    </div>
    <div class="nav-item" style="left:395px;top:10px">
      <svg width="17" height="17" viewBox="0 0 17 17"><circle cx="8.5" cy="8.5" r="8.5" fill="#fff"/><path d="M6 5.5l3 3-3 3M9 5.5l3 3-3 3" stroke="#f5640f" stroke-width="1.2" fill="none"/></svg>
      <span>OTHER SERVICE</span>
    </div>
    <div class="nav-item" style="left:25px;top:50px">
      <svg width="17" height="17" viewBox="0 0 17 17"><circle cx="8.5" cy="8.5" r="8.5" fill="#fff"/><path d="M6 5.5l3 3-3 3M9 5.5l3 3-3 3" stroke="#f5640f" stroke-width="1.2" fill="none"/></svg>
      <span>ABOUT US</span>
    </div>
    <div class="nav-item" style="left:170px;top:50px">
      <svg width="17" height="17" viewBox="0 0 17 17"><circle cx="8.5" cy="8.5" r="8.5" fill="#fff"/><path d="M6 5.5l3 3-3 3M9 5.5l3 3-3 3" stroke="#f5640f" stroke-width="1.2" fill="none"/></svg>
      <span>RESIDENTIAL SERVICE</span>
    </div>
    <div class="nav-item" style="left:395px;top:50px">
      <svg width="17" height="17" viewBox="0 0 17 17"><circle cx="8.5" cy="8.5" r="8.5" fill="#fff"/><path d="M6 5.5l3 3-3 3M9 5.5l3 3-3 3" stroke="#f5640f" stroke-width="1.2" fill="none"/></svg>
      <span>CONTACT US</span>
    </div>
  </nav>

  <div class="hero abs" role="img" aria-label="Photo of a large white house with a tiled roof and garden"></div>

  <section class="feature residential abs">
    <div class="feature-thumb" role="img" aria-label="Photo of a tall residential apartment building"></div>
    <div class="feature-title">RESIDENTIAL<br>BUILDINGS</div>
    <span class="btn">More &gt;</span>
  </section>
  <section class="feature commercial abs">
    <div class="feature-thumb" role="img" aria-label="Photo of a glass commercial tower"></div>
    <div class="feature-title">COMMERCIAL<br>BUILDINGS</div>
    <span class="btn">More &gt;</span>
  </section>
  <section class="feature experience abs">
    <div class="feature-thumb" role="img" aria-label="Photo of a modern commercial complex"></div>
    <div class="feature-title">OUR<br>EXPERIENCE</div>
    <span class="btn">More &gt;</span>
  </section>

  <main class="content abs"></main>

  <h2 class="section-title welcome-title abs">WELCOME TO VERDANT WATT</h2>
  <div class="welcome-body abs">
    <div class="welcome-thumb" role="img" aria-label="Photo of an apartment block"></div>
    Verdant Watt is an innovator in energy assessment for commercial and residential buildings. We have a wealth of experience in helping our clients create more energy efficient and environmentally sustainable buildings which is not only mandatory, but will lower your utility bills and increase your resale value. Verdant Watt is an affiliation between SunLedger and ClearPane Studio because both companies wish to provide our clients with a broad range of expertise and a range of services and products.
  </div>
  <span class="btn welcome-more">More</span>

  <div class="divider abs"></div>

  <h2 class="section-title services-title abs">SERVICES</h2>
  <ul class="service-list first">
    <li><svg width="7" height="10" viewBox="0 0 7 10"><path d="M1 1l4 4-4 4" stroke="#3d2a0c" stroke-width="1.3" fill="none"/></svg>Initial design consultation.</li>
    <li><svg width="7" height="10" viewBox="0 0 7 10"><path d="M1 1l4 4-4 4" stroke="#3d2a0c" stroke-width="1.3" fill="none"/></svg>Sketch designs and energy assessment.</li>
    <li><svg width="7" height="10" viewBox="0 0 7 10"><path d="M1 1l4 4-4 4" stroke="#3d2a0c" stroke-width="1.3" fill="none"/></svg>Final consultation and design.</li>
    <li><svg width="7" height="10" viewBox="0 0 7 10"><path d="M1 1l4 4-4 4" stroke="#3d2a0c" stroke-width="1.3" fill="none"/></svg>Building Fabric.</li>
    <li><svg width="7" height="10" viewBox="0 0 7 10"><path d="M1 1l4 4-4 4" stroke="#3d2a0c" stroke-width="1.3" fill="none"/></svg>Full drafting.</li>
    <li><svg width="7" height="10" viewBox="0 0 7 10"><path d="M1 1l4 4-4 4" stroke="#3d2a0c" stroke-width="1.3" fill="none"/></svg>Development approval.</li>
    <li><svg width="7" height="10" viewBox="0 0 7 10"><path d="M1 1l4 4-4 4" stroke="#3d2a0c" stroke-width="1.3" fill="none"/></svg>Construction documentation.</li>
    <li><svg width="7" height="10" viewBox="0 0 7 10"><path d="M1 1l4 4-4 4" stroke="#3d2a0c" stroke-width="1.3" fill="none"/></svg>Entity consultation electrical, water, drainage.</li>
    <li><svg width="7" height="10" viewBox="0 0 7 10"><path d="M1 1l4 4-4 4" stroke="#3d2a0c" stroke-width="1.3" fill="none"/></svg>Building Sealing.</li>
  </ul>
  <ul class="service-list second">
    <li><svg width="7" height="10" viewBox="0 0 7 10"><path d="M1 1l4 4-4 4" stroke="#3d2a0c" stroke-width="1.3" fill="none"/></svg>Municipal services approvals.</li>
    <li><svg width="7" height="10" viewBox="0 0 7 10"><path d="M1 1l4 4-4 4" stroke="#3d2a0c" stroke-width="1.3" fill="none"/></svg>Development application and management.</li>
    <li><svg width="7" height="10" viewBox="0 0 7 10"><path d="M1 1l4 4-4 4" stroke="#3d2a0c" stroke-width="1.3" fill="none"/></svg>Air-Conditioning and Ventilation Systems.</li>
    <li><svg width="7" height="10" viewBox="0 0 7 10"><path d="M1 1l4 4-4 4" stroke="#3d2a0c" stroke-width="1.3" fill="none"/></svg>Development application and management.</li>
    <li><svg width="7" height="10" viewBox="0 0 7 10"><path d="M1 1l4 4-4 4" stroke="#3d2a0c" stroke-width="1.3" fill="none"/></svg>Artificial Lighting and Power.</li>
    <li><svg width="7" height="10" viewBox="0 0 7 10"><path d="M1 1l4 4-4 4" stroke="#3d2a0c" stroke-width="1.3" fill="none"/></svg>Hot Water Supply.</li>
    <li><svg width="7" height="10" viewBox="0 0 7 10"><path d="M1 1l4 4-4 4" stroke="#3d2a0c" stroke-width="1.3" fill="none"/></svg>Access for Maintenance.</li>
    <li><svg width="7" height="10" viewBox="0 0 7 10"><path d="M1 1l4 4-4 4" stroke="#3d2a0c" stroke-width="1.3" fill="none"/></svg>External Glazing.</li>
  </ul>
  <span class="btn services-more">More</span>

  <footer class="footer-band abs"></footer>

  <section class="info-panel abs">
    <span class="col-rule" style="left:155px"></span>
    <span class="col-rule" style="left:376px"></span>
    <span class="col-rule" style="left:605px"></span>

    <h3 class="panel-title" style="left:18px">NAVIGATION</h3>
    <ul class="link-list">
      <li><svg width="6" height="9" viewBox="0 0 6 9"><path d="M1 1l3.5 3.5L1 8" stroke="#3d2a0c" stroke-width="1.2" fill="none"/></svg>Home</li>
      <li><svg width="6" height="9" viewBox="0 0 6 9"><path d="M1 1l3.5 3.5L1 8" stroke="#3d2a0c" stroke-width="1.2" fill="none"/></svg>About Us</li>
      <li><svg width="6" height="9" viewBox="0 0 6 9"><path d="M1 1l3.5 3.5L1 8" stroke="#3d2a0c" stroke-width="1.2" fill="none"/></svg>Commercial service</li>
      <li><svg width="6" height="9" viewBox="0 0 6 9"><path d="M1 1l3.5 3.5L1 8" stroke="#3d2a0c" stroke-width="1.2" fill="none"/></svg>Residential Service</li>
      <li><svg width="6" height="9" viewBox="0 0 6 9"><path d="M1 1l3.5 3.5L1 8" stroke="#3d2a0c" stroke-width="1.2" fill="none"/></svg>Other Service</li>
      <li><svg width="6" height="9" viewBox="0 0 6 9"><path d="M1 1l3.5 3.5L1 8" stroke="#3d2a0c" stroke-width="1.2" fill="none"/></svg>Contact US</li>
    </ul>

    <h3 class="panel-title" style="left:180px">LATEST NEWS</h3>
    <div class="news-item" style="top:69px">
      <div class="news-date">FEB<b>5</b></div>
      <div class="news-text">The Federal Government has recently Energy commercial..</div>
    </div>
    <div class="news-item" style="top:129px">
      <div class="news-date">FEB<b>6</b></div>
      <div class="news-text">The Federal Government has recently Energy commercial..</div>
    </div>
    <span class="pager" style="left:298px;background:#1a1208"><svg width="12" height="10" viewBox="0 0 12 10"><path d="M6 1L2 5l4 4M10 1L6 5l4 4" stroke="#fff" stroke-width="1.4" fill="none"/></svg></span>
    <span class="pager" style="left:331px;background:#3d2103"><svg width="12" height="10" viewBox="0 0 12 10"><path d="M2 1l4 4-4 4M6 1l4 4-4 4" stroke="#fff" stroke-width="1.4" fill="none"/></svg></span>

    <h3 class="panel-title" style="left:398px">GENERAL ENQUIRIES</h3>
    <div class="enquiry">
      <div>PO BOX XX Wattlefield</div>
      <div>ACT 2999</div>
      <div class="row"><span class="k">Phone</span><span class="s">:</span><span>02 6000 1234</span></div>
      <div class="row"><span class="k">Tom (mobile)</span><span class="s">:</span><span>0400 111 222</span></div>
      <div class="row"><span class="k">Clara (mobile)</span><span class="s">:</span><span>0400 333 444</span></div>
      <div>E :tom.reed@verdantwatt.example</div>
      <div>clara.hale@verdantwatt.example</div>
    </div>

    <h3 class="panel-title" style="left:616px">QUICK CONTACT</h3>
    <span class="form-label" style="top:68px">Name :</span>
    <span class="field" style="top:64px"></span>
    <span class="form-label" style="top:93px">Phone :</span>
    <span class="field" style="top:89px"></span>
    <span class="form-label" style="top:118px">E-mail :</span>
    <span class="field" style="top:114px"></span>
    <span class="form-label" style="top:143px">Comment :</span>
    <span class="field" style="top:139px;height:47px"></span>
    <span class="btn submit">Submit</span>
  </section>

  <div class="copyright abs">2012@ Allright Reserved.</div>
  <span class="social abs" style="left:892px"></span>
  <span class="social abs" style="left:926px"></span>
  <span class="social abs" style="left:960px"></span>

</div>
</body>
</html>
```